Business Card Design

A business card design must match as a cleaning company.
We do house cleaning, office, cafe , function center , club and so on.

Industry/Entity Type

House

Contact Information for Business Card

Bright Lane cleaning services
Mara Delvin
Director
0428395146
1300 917 254
Brightlane.cleaning@bluvex.com

```html
<!DOCTYPE html>
<html lang="en">
<head>
<meta charset="UTF-8">
<title>Bright Lane Cleaning Services – Business Card</title>
<link rel="stylesheet" href="https://fonts.googleapis.com/css2?family=Arimo:wght@400;700&display=swap">
<style>
  :root {
    --backdrop: #808184;
    --card: #ffffff;
    --ink: #111111;
    --wave-blue-dark: #0b6fba;
    --wave-blue-light: #2fb0e6;
    --wave-grey-dark: #8d8e91;
    --wave-grey-light: #cfd0d2;
    --art-blue: #3f8fd0;
    --art-grey: #6d6f73;
  }
  * { margin: 0; padding: 0; box-sizing: border-box; }
  html, body {
    width: 1200px;
    height: 900px;
    overflow: hidden;
    background: var(--backdrop);
  }
  .canvas {
    position: relative;
    width: 1200px;
    height: 900px;
  }
  .business-card {
    position: absolute;
    left: 292px;
    top: 265px;
    width: 666px;
    height: 383px;
    background: var(--card);
    overflow: hidden;
    font-family: "Arimo", Arial, sans-serif;
    color: var(--ink);
  }
  .wave {
    position: absolute;
    left: 0;
    top: 0;
    width: 666px;
    height: 383px;
  }
  .product-art {
    position: absolute;
    left: 46px;
    top: 70px;
    width: 146px;
    height: 174px;
    border-radius: 36px 36px 22px 22px;
    background: linear-gradient(160deg, var(--art-blue) 0%, #2a6fb0 55%, var(--art-grey) 100%);
  }
  .company-name {
    position: absolute;
    left: 206px;
    top: 53px;
    font-size: 24px;
    line-height: 30px;
    font-weight: 700;
    letter-spacing: -0.6px;
    white-space: nowrap;
    text-transform: uppercase;
  }
  .person-name {
    position: absolute;
    left: 337px;
    top: 96px;
    font-size: 25px;
    line-height: 30px;
    font-weight: 700;
    letter-spacing: -0.5px;
    white-space: nowrap;
    text-transform: uppercase;
  }
  .person-role {
    position: absolute;
    left: 417px;
    top: 126px;
    font-size: 22px;
    line-height: 26px;
    font-weight: 400;
    white-space: nowrap;
  }
  .contact {
    position: absolute;
    left: 260px;
    top: 179px;
    font-size: 18px;
    line-height: 29px;
    white-space: nowrap;
  }
  .contact-label {
    margin-right: 8px;
  }
</style>
</head>
<body>
<main class="canvas">
  <section class="business-card">
    <svg class="wave" viewBox="0 0 666 383" aria-hidden="true">
      <defs>
        <linearGradient id="grey-sweep" x1="0" y1="0" x2="1" y2="0">
          <stop offset="0" stop-color="var(--wave-grey-light)"/>
          <stop offset="0.5" stop-color="var(--wave-grey-dark)"/>
          <stop offset="1" stop-color="var(--wave-grey-light)"/>
        </linearGradient>
        <linearGradient id="blue-sweep" x1="0" y1="1" x2="1" y2="0">
          <stop offset="0" stop-color="var(--wave-blue-dark)"/>
          <stop offset="1" stop-color="var(--wave-blue-light)"/>
        </linearGradient>
      </defs>
      <path d="M0,383 C60,318 130,272 230,262 C330,252 420,258 500,228 C560,205 620,182 666,172 L666,383 Z" fill="url(#grey-sweep)"/>
      <path d="M0,383 C70,332 150,292 240,282 C340,272 420,276 510,250 C580,230 630,210 666,202 L666,383 Z" fill="url(#blue-sweep)"/>
    </svg>

    <div class="product-art" role="img" aria-label="Illustration of a blue canister vacuum cleaner with hose and wand"></div>

    <h1 class="company-name">Bright Lane Cleaning Services</h1>
    <h2 class="person-name">Mara Delvin</h2>
    <p class="person-role">Director</p>

    <div class="contact">
      <p><span class="contact-label">PHONE NO:</span>0428395146 1300 917 254</p>
      <p><span class="contact-label">E.MAIL:</span>Brightlane.cleaning@bluvex.com</p>
    </div>
  </section>
</main>
</body>
</html>
```